The Pulp Corner- 2026 Menu- Drinks/Food

We are The Pulp Corner, a premium NYC-inspired juice bar.
We need two matching 4K TV menu designs with a clean, modern New York feel.
TV 1 – DRINKS
Cold-Pressed Juices, Smoothies, and Coffee/Espresso.
TV 2 – FOOD
Bowls, Toasts, Wraps, Hot Food, and Treats/Sweets.
The menus should feel bold, minimal, and easy to read from a distance.
Strong typography is preferred over heavy photos. The two screens must clearly match as one brand while serving different purposes.
Designs must be optimized for 4K TVs and in a NYC style (subtle subway / street influence, not cartoonish).
This is what we have now. We are updating items and prices along with changing some items.
I have some changes we’d like to do also. But this is what we are using now

```html
<!DOCTYPE html>
<html lang="en">
<head>
<meta charset="utf-8">
<title>The Pulp Corner – Drinks & Food Menu</title>
<link href="https://fonts.googleapis.com/css2?family=Oswald:wght@500;700&family=Montserrat:wght@400;600;700&family=Yellowtail&display=swap" rel="stylesheet">
<style>
:root{
  --stage:#3e3e3e;
  --board:#f2f2f0;
  --board-edge:#e6e6e3;
  --green:#78a02a;
  --green-dark:#5f8419;
  --slate:#3b4148;
  --ink:#3c3c3c;
  --muted:#555;
  --panel:#f7f7f6;
  --white:#ffffff;
}
*{margin:0;padding:0;box-sizing:border-box}
html,body{width:820px;height:1200px;overflow:hidden}
body{background:var(--stage);font-family:"Montserrat",Arial,sans-serif;color:var(--ink);position:relative}

.board{position:absolute;left:69px;width:681px;height:384px;background:linear-gradient(135deg,var(--board) 0%,var(--board-edge) 100%);overflow:hidden}
.board--drinks{top:157px}
.board--food{top:639px}
.board > *{position:absolute;z-index:1}
.board > .photo{z-index:0}

.photo{display:block}
.section-title{font-family:"Oswald",Arial,sans-serif;font-weight:500;color:var(--green);font-size:15px;letter-spacing:.2px;line-height:1;text-transform:uppercase}

.brand{left:228px;top:36px;display:flex;align-items:center;gap:6px}
.brand-dot{width:14px;height:14px;border-radius:50%;background:var(--green);flex:none}
.brand-name{font-family:"Oswald",Arial,sans-serif;font-weight:700;font-size:15px;color:var(--slate);text-transform:uppercase;line-height:1.05}

.headline{top:22px;display:flex;align-items:center;gap:10px;white-space:nowrap}
.headline-script{font-family:"Yellowtail",cursive;font-weight:400;color:var(--green);font-size:54px;line-height:1}
.headline-block{font-family:"Oswald",Arial,sans-serif;font-weight:700;color:var(--slate);font-size:56px;line-height:1;letter-spacing:-1px}
.board--drinks .headline{left:317px}
.board--food .headline{left:309px}

/* item lists */
.list{display:flex;flex-direction:column;justify-content:space-between}
.item{display:grid;grid-template-columns:1fr 14px;column-gap:6px;align-items:start}
.item-name{font-weight:700;font-size:4.6px;line-height:1.25;text-transform:uppercase;color:var(--ink)}
.item-desc{font-size:4.5px;line-height:1.3;color:var(--muted)}
.tag{width:14px;height:11px;background:var(--green);color:var(--white);font-size:3.8px;font-weight:700;display:flex;align-items:flex-start;justify-content:center;padding-top:2.5px;clip-path:polygon(0 0,100% 0,100% 100%,50% 78%,0 100%)}

.organic-note{left:45px;width:120px;height:28px;background:var(--green);color:var(--white);font-size:4.8px;font-weight:700;display:flex;flex-direction:column;align-items:center;justify-content:center;gap:2px;text-align:center}
.web{left:56px;top:351px;display:flex;align-items:center;gap:5px;font-weight:600;font-size:11px;color:var(--green)}
.web svg{width:8px;height:8px}
.social{left:508px;top:351px;display:flex;align-items:center;gap:5px;font-weight:700;font-size:11.5px;color:var(--green)}
.social-dot{width:7px;height:7px;border-radius:50%;background:var(--slate)}

.menu-panel{border:2px solid var(--green);border-radius:7px;background:var(--panel)}
.panel-cols{display:grid;grid-template-columns:1fr 1fr;column-gap:26px;height:100%}
.panel-cols .item{grid-template-columns:1fr 14px;column-gap:10px}

.service-strip{width:262px;height:25px;display:grid;grid-template-columns:128px 1fr;border:1px solid var(--green);background:var(--white)}
.service-strip p{font-size:5px;line-height:1.35;display:flex;flex-direction:column;justify-content:center;padding-left:6px}
.service-strip .strip-alt{background:var(--green);color:var(--white)}
.service-strip b{font-weight:700}

/* drinks board */
.photo-strawberry{left:0;top:0;width:42px;height:48px;background:radial-gradient(circle at 45% 45%,#d63a2f,#a51d1a 70%,#c9e0b0 100%);border-radius:0 0 50% 0}
.photo-orange{left:0;top:126px;width:34px;height:70px;background:radial-gradient(circle at 0 50%,#ffd07a 0,#f59a1b 55%,#e07d0c 100%);border-radius:0 35px 35px 0}
.photo-jar{left:0;top:266px;width:46px;height:115px;background:linear-gradient(180deg,#f3c9cf 0%,#d64550 40%,#b42a33 100%);border-radius:0 14px 10px 0}
.photo-avocado-shake{left:594px;top:0;width:87px;height:102px;background:radial-gradient(circle at 60% 35%,#dfe8a8 0,#b9cc6b 45%,#4d6b22 80%,#5a3a1c 100%);border-radius:0 0 0 40px}
.photo-coffee{left:596px;top:270px;width:80px;height:74px;background:radial-gradient(circle at 50% 50%,#e9d3b4 0,#c8a377 35%,#2b2320 60%,#4a3322 100%);border-radius:50%}

.juices-title{left:48px;top:32px}
.juices{left:48px;top:52px;width:161px;height:248px}
.drinks-organic{top:313px}

.smoothies-panel{left:233px;top:100px;width:428px;height:182px;padding:8px 10px 8px 18px}
.smoothies-panel .section-title{font-size:16px;margin-bottom:6px}
.smoothies-panel .panel-cols{height:auto}
.smoothies-left{height:148px;margin-top:-2px}
.smoothies-right{height:168px;margin-top:-22px}

.coffee-title{left:235px;top:289px}
.coffee-row{left:235px;top:307px;display:flex;gap:12px;align-items:flex-start}
.coffee-row .item-desc{width:88px}
.coffee-sizes{font-size:4.5px;line-height:1.3;color:var(--muted);width:22px}
.water{display:flex;gap:10px;align-items:flex-start}
.water .item-name{padding-top:1px}
.drinks-strip{left:233px;top:336px}

/* food board */
.photo-strawberry-food{left:0;top:0;width:42px;height:48px;background:radial-gradient(circle at 45% 45%,#d63a2f,#a51d1a 70%,#c9e0b0 100%);border-radius:0 0 50% 0}
.photo-bowl{left:0;top:124px;width:40px;height:74px;background:radial-gradient(circle at 20% 50%,#efe6d6 0,#c9a27a 45%,#b7323a 75%,#f4f1ec 100%);border-radius:0 37px 37px 0}
.photo-avocado{left:0;top:306px;width:58px;height:72px;background:radial-gradient(circle at 55% 50%,#6b3a1c 0,#6b3a1c 18%,#dfe59a 20%,#a9c258 55%,#3e5a1e 80%);border-radius:0 45% 45% 0}
.photo-toast{left:578px;top:0;width:103px;height:103px;background:linear-gradient(135deg,#c99a62 0%,#86b34a 45%,#e7c0c4 70%,#b07a45 100%);border-radius:0 0 0 50px}
.photo-bagel{left:613px;top:275px;width:68px;height:65px;background:radial-gradient(circle at 50% 50%,#f6efe3 0,#f08a5d 35%,#8bb04a 55%,#c99452 75%);border-radius:40% 0 0 40%}

.toasts-title{left:48px;top:32px}
.toasts{left:48px;top:52px;width:161px;height:252px}
.custom-note{font-size:4.5px;color:var(--muted);line-height:1.3}
.custom-note b{color:var(--ink);font-weight:700;display:block}
.food-organic{top:315px;width:166px}

.bowls-panel{left:223px;top:99px;width:433px;height:131px;padding:8px 10px 8px 18px}
.bowls-panel .section-title{font-size:16px;margin-bottom:5px}
.bowls-left{height:96px;margin-top:-2px}
.bowls-right{height:114px;margin-top:-19px}

.treats-title{left:223px;top:246px}
.treats{left:223px;top:262px;width:187px;height:72px}
.hot-panel{left:420px;top:243px;width:261px;height:90px;background:var(--green);padding:9px 14px}
.hot-panel .section-title{color:var(--white);font-size:16px;margin-bottom:5px}
.hot-cols{display:grid;grid-template-columns:92px 92px;column-gap:14px}
.hot-row{display:flex;justify-content:space-between;font-size:4.6px;line-height:1.5;color:var(--white)}
.food-strip{left:223px;top:338px}
</style>
</head>
<body>

<section class="board board--drinks" aria-label="Drinks menu board">
  <div class="photo photo-strawberry" role="img" aria-label="Fresh strawberries with leaves"></div>
  <div class="photo photo-orange" role="img" aria-label="Halved orange slice"></div>
  <div class="photo photo-jar" role="img" aria-label="Strawberry smoothie in a jar"></div>
  <div class="photo photo-avocado-shake" role="img" aria-label="Avocado smoothie with halved avocado"></div>
  <div class="photo photo-coffee" role="img" aria-label="Cup of coffee with beans"></div>

  <h2 class="section-title juices-title">Cold-Pressed Juices</h2>
  <div class="list juices">
    <div class="item"><div><p class="item-name">Hot Bam (S)</p><p class="item-desc">Red Apple, Lemon, Ginger, Cayenne Pepper</p></div><span class="tag">$12.50</span></div>
    <div class="item"><div><p class="item-name">Sunset Park</p><p class="item-desc">Orange, Carrot Celery</p></div><span class="tag">$12.50</span></div>
    <div class="item"><div><p class="item-name">Lean Green</p><p class="item-desc">Spinach, Celery, Cucumber, Romaine, Lemon, Himalayan Pink Salt Celery</p></div><span class="tag">$12.50</span></div>
    <div class="item"><div><p class="item-name">Revive</p><p class="item-desc">Cantaloupe, Red Apple, Lemon</p></div><span class="tag">$12.50</span></div>
    <div class="item"><div><p class="item-name">Renew</p><p class="item-desc">Coconut Water, Red Apple, Blueberry, Grape</p></div><span class="tag">$12.50</span></div>
    <div class="item"><div><p class="item-name">Vida</p><p class="item-desc">Beet, Raspberry, Red Apple, Orange</p></div><span class="tag">$12.50</span></div>
    <div class="item"><div><p class="item-name">The Breakdown</p><p class="item-desc">Carrot, Red Apple, Ginger, Beet, Lemon, Pineapple</p></div><span class="tag">$12.50</span></div>
    <div class="item"><div><p class="item-name">Green Goddess</p><p class="item-desc">Spinach, Celery, Cucumber, Romaine, Kale, Parsley, Green Cabbage</p></div><span class="tag">$12.50</span></div>
    <div class="item"><div><p class="item-name">Sunny Day</p><p class="item-desc">Pineapple, Lemon, Orange, Ginger</p></div><span class="tag">$12.50</span></div>
    <div class="item"><div><p class="item-name">Glow Up</p><p class="item-desc">Celery, Lime</p></div><span class="tag">$12.50</span></div>
    <div class="item"><div><p class="item-name">Sailor's Delight</p><p class="item-desc">Spinach, Orange, Pear, Green Apple, Ginger</p></div><span class="tag">$12.50</span></div>
    <div class="item"><div><p class="item-name">Classic (shot)</p><p class="item-desc">Ginger, Lemon</p></div><span class="tag">$6.00</span></div>
    <div class="item"><div><p class="item-name">Sunshine (shot)</p><p class="item-desc">Ginger, Lemon, Red Apple, Turmeric, Black Pepper</p></div><span class="tag">$6.00</span></div>
    <div class="item"><div><p class="item-name">Heavy Hitter (shot)</p><p class="item-desc">Ginger, Lemon, Cayenne Pepper, Spinach, Green Applepeel</p></div><span class="tag">$6.00</span></div>
    <div class="item"><div><p class="item-name">Detox (shot)</p><p class="item-desc">Wheatgrass</p></div><span class="tag">$6.00</span></div>
  </div>

  <div class="organic-note drinks-organic"><span>100% Organic Fruits and Vegetables</span><span>(V) Vegan (S) Spicy</span></div>
  <p class="web"><svg viewBox="0 0 10 10" aria-hidden="true"><circle cx="5" cy="5" r="4.2" fill="none" stroke="#3b4148" stroke-width="1.2"/><path d="M1 5h8M5 1c-2 2.5-2 5.5 0 8M5 1c2 2.5 2 5.5 0 8" fill="none" stroke="#3b4148" stroke-width=".8"/></svg>www.thepulpcorner.net</p>

  <div class="brand"><span class="brand-dot"></span><span class="brand-name">The Pulp<br>Corner</span></div>
  <div class="headline"><h1 class="headline-script">Drinks</h1><p class="headline-block">MENU</p></div>

  <div class="menu-panel smoothies-panel">
    <h2 class="section-title">Smoothies</h2>
    <div class="panel-cols">
      <div class="list smoothies-left">
        <div class="item"><div><p class="item-name">Spring Street</p><p class="item-desc">Coconut Water, Blueberries, Pineapple, Spinach, Honey, Hemp Hearts</p></div><span class="tag">$13.00</span></div>
        <div class="item"><div><p class="item-name">Flushing Ave</p><p class="item-desc">Coconut Milk, Spinach, Kale, Strawberries, Pineapple, Chia Seeds, Hemp Hearts</p></div><span class="tag">$13.00</span></div>
        <div class="item"><div><p class="item-name">Fort Greene</p><p class="item-desc">Almond Milk, Bananas, Mango, Avocado, Spinach, Kale, Honey</p></div><span class="tag">$13.00</span></div>
        <div class="item"><div><p class="item-name">Jimmy The Leafy Giant</p><p class="item-desc">Coconut Milk, Bananas, Strawberries, Kale, Sea Moss Gel, Green Spirulina</p></div><span class="tag">$13.00</span></div>
        <div class="item"><div><p class="item-name">Atlantic Terminal</p><p class="item-desc">Almond Milk, Bananas, Strawberries, Blueberries, Pineapple, Coconut Shavings; Choice of 1 of the following: Peanut, Almond, Cashew Butter and/or Hazelnut Spread, Honey, Chia Seeds, Bee Pollen</p></div><span class="tag">$13.00</span></div>
        <div class="item"><div><p class="item-name">Build Your Own</p><p class="item-desc">1 liquid base: Almond, Coconut, Oat Milk, Orange, Apple Juice, Coconut Water, Filtered Water; Choice of 3 Fruits and/or Vegetables</p></div><span class="tag">$12.00</span></div>
      </div>
      <div class="list smoothies-right">
        <div class="item"><div><p class="item-name">Union Square</p><p class="item-desc">Almond Milk, Grade A Açaí, Bananas, Strawberries, Blueberries, Pineapple, Coconut Oil</p></div><span class="tag">$13.00</span></div>
        <div class="item"><div><p class="item-name">Grand Central</p><p class="item-desc">Almond Milk, Grade A Açaí, Bananas, Blueberries, Granola, Cacao Nibs; Choice of 1 of the following: Peanut, Almond, Cashew Butter and/or Hazelnut Spread</p></div><span class="tag">$13.00</span></div>
        <div class="item"><div><p class="item-name">P.S. 124</p><p class="item-desc">1 liquid base: Almond, Coconut and/or Oat Milk, Orange Juice, Apple Juice or Coconut Water; Bananas and Strawberries</p></div><span class="tag">$12.00</span></div>
        <div class="item"><div><p class="item-name">Lexington Avenue</p><p class="item-desc">Coconut Milk, Strawberries, Bananas, Raspberries, Kiwi, Vanilla Yogurt</p></div><span class="tag">$12.50</span></div>
        <div class="item"><div><p class="item-name">Power Up</p><p class="item-desc">Almond Milk, Bananas, Strawberries, Raspberries, Peanut Butter, Cacao Nibs</p></div><span class="tag">$13.00</span></div>
        <div class="item"><div><p class="item-name">The Peanut</p><p class="item-desc">Almond Milk, Bananas, Peanut Butter, Cinnamon, Chocolate Plant Protein</p></div><span class="tag">$12.50</span></div>
      </div>
    </div>
  </div>

  <h2 class="section-title coffee-title">Coffee/Espresso</h2>
  <div class="coffee-row">
    <div><p class="item-name">Cold Brew Coffee</p><p class="item-desc">Almond Milk, Coconut Milk, Agave or Vanilla</p></div>
    <p class="coffee-sizes">(12 oz)<br>(12 oz)<br>(each)</p>
    <span class="tag">$5.00</span>
    <div class="water" style="margin-left:8px"><p class="item-name">Alkaline Water</p><span class="tag">$3.00</span></div>
    <div class="water" style="margin-left:8px"><p class="item-name">Coconut Water</p><span class="tag">$3.50</span></div>
  </div>

  <div class="service-strip drinks-strip">
    <p><span><b>12 Oz Juices</b> and <b>2 Oz Shots</b></span><span>served in glass bottles.</span></p>
    <p class="strip-alt"><span><b>Gallon</b> and <b>1/2 Gallon</b> of our signature juices</span><span>available upon request.</span></p>
  </div>
  <p class="social"><span class="social-dot"></span>ThePulpCorner561</p>
</section>

<section class="board board--food" aria-label="Food menu board">
  <div class="photo photo-strawberry-food" role="img" aria-label="Fresh strawberries with leaves"></div>
  <div class="photo photo-bowl" role="img" aria-label="Granola bowl with strawberries"></div>
  <div class="photo photo-avocado" role="img" aria-label="Halved avocado with pit"></div>
  <div class="photo photo-toast" role="img" aria-label="Avocado toast topped with radish and greens"></div>
  <div class="photo photo-bagel" role="img" aria-label="Bagel sandwich with smoked salmon"></div>

  <h2 class="section-title toasts-title">Toasts &amp; Wraps</h2>
  <div class="list toasts">
    <div class="item"><div><p class="item-name">The Patriot</p><p class="item-desc">Seedy Sourdough Bread, Choice of Peanut, Almond, Cashew Butter or Hazelnut Spread, Strawberries, Bananas, Blueberries, Honey, Hemp Hearts</p></div><span class="tag">$13.25</span></div>
    <div class="item"><div><p class="item-name">Avocado Toast</p><p class="item-desc">Seedy Sourdough Bread, Whole Avocado, Everything Bagel Seasoning, Honey</p></div><span class="tag">$14.00</span></div>
    <div class="item"><div><p class="item-name">Breakfast Toast</p><p class="item-desc">Seedy Sourdough Bread, Smashed Avocado, Hardboiled Eggs, Red Onion, Lemon Juice, Himalayan Pink Salt, Pepper, Everything Bagel Seasoning</p></div><span class="tag">$14.50</span></div>
    <div class="item"><div><p class="item-name">Smoked Salmon Toast</p><p class="item-desc">Seedy Sourdough Bread, Smoked Wild Salmon, Tamari Sauce, Avocado, Cucumber, Leafy Greens, Everything Bagel Seasoning</p></div><span class="tag">$16.00</span></div>
    <div class="item"><div><p class="item-name">Turmeric Chicken Salad</p><p class="item-desc">Wholewheat Sprouted Grain Wrap, Mayo, Chicken Breast, Red Onion, Cucumber, Carrots, Leafy Greens, Served with Balsamic Vinegar Dressing</p></div><span class="tag">$15.00</span></div>
    <div class="item"><div><p class="item-name">Elite Wild Tuna Salad</p><p class="item-desc">Wholewheat Sprouted Grain Wrap, Mayo, Wild Tuna, Red Onion, Celery, Leafy Greens</p></div><span class="tag">$16.00</span></div>
    <div class="item"><div><p class="item-name">Spicy Chickpea Salad (V)(S)</p><p class="item-desc">Wholewheat Sprouted Grain Wrap, Tomatillo Sriracha, Chickpeas, Toasted Sesame Seeds, Red Pepper Hummus, Leafy Greens</p></div><span class="tag">$14.00</span></div>
    <p class="custom-note"><b>*Custom Salads</b>Available upon request depending on availability</p>
  </div>

  <div class="organic-note food-organic"><span>100% Organic Fruits and Vegetables</span><span>(V) Vegan (S) Spicy</span></div>
  <p class="web"><svg viewBox="0 0 10 10" aria-hidden="true"><circle cx="5" cy="5" r="4.2" fill="none" stroke="#3b4148" stroke-width="1.2"/><path d="M1 5h8M5 1c-2 2.5-2 5.5 0 8M5 1c2 2.5 2 5.5 0 8" fill="none" stroke="#3b4148" stroke-width=".8"/></svg>www.thepulpcorner.net</p>

  <div class="brand"><span class="brand-dot"></span><span class="brand-name">The Pulp<br>Corner</span></div>
  <div class="headline"><h1 class="headline-script">Food</h1><p class="headline-block">MENU</p></div>

  <div class="menu-panel bowls-panel">
    <h2 class="section-title">Bowls</h2>
    <div class="panel-cols">
      <div class="list bowls-left">
        <div class="item"><div><p class="item-name">Park Slope</p><p class="item-desc">Grade A Açaí, Granola, Bananas, Honey</p></div><span class="tag">$13.50</span></div>
        <div class="item"><div><p class="item-name">Bay Ridge</p><p class="item-desc">Grade A Açaí, Granola, Bananas, Strawberries, Blueberries, Honey</p></div><span class="tag">$14.00</span></div>
        <div class="item"><div><p class="item-name">Bushwick</p><p class="item-desc">Grade A Açaí, Granola, Bananas, Pineapple, Fresh Coconut Meat, Honey, Bee Pollen</p></div><span class="tag">$14.25</span></div>
        <div class="item"><div><p class="item-name">Build Your Own</p><p class="item-desc">Grade A Açaí, Granola, 2 Organic Fruits, Honey</p></div><span class="tag">$14.00</span></div>
        <div class="item"><div><p class="item-name">The Village</p><p class="item-desc">Grade A Açaí, Granola, Bananas, Strawberries, Kiwi, Pineapple, Blueberries, Coconut Shavings, Honey, Hemp Hearts</p></div><span class="tag">$14.25</span></div>
      </div>
      <div class="list bowls-right">
        <div class="item"><div><p class="item-name">Pink Dragon</p><p class="item-desc">Apple Juice blended w/ Pitaya, Bananas, Strawberries. Layered w/ Granola, Strawberries, Pineapple, Blueberries, Coconut Flakes, Honey, Hemp Hearts</p></div><span class="tag">$14.00</span></div>
        <div class="item"><div><p class="item-name">Coco Loco</p><p class="item-desc">Coconut Milk blended w/ Coconut Chunks, Bananas, Honey. Layered w/ Granola, Pineapple, Seasonal Fruit, Fresh Coconut Meat, Coconut Flakes, Honey, Hemp Hearts</p></div><span class="tag">$14.00</span></div>
        <div class="item"><div><p class="item-name">Coney Island</p><p class="item-desc">Apple Juice blended w/ Jackfruit, Mango and Pineapple. Layered w/ Granola, Bananas, Strawberries, Pineapple, Honey</p></div><span class="tag">$14.00</span></div>
        <div class="item"><div><p class="item-name">Main Street $14.00</p><p class="item-desc">Grade A Açaí, Choice of 1 of the following: Peanut, Almond, Cashew Butter and/or Hazelnut Spread, Granola, Bananas, Honey, Cacao Nibs, Hemp Hearts</p></div><span class="tag">$14.00</span></div>
      </div>
    </div>
  </div>

  <h2 class="section-title treats-title">Treats/Sweets.</h2>
  <div class="list treats">
    <div class="item"><div><p class="item-name">Coco Loco</p><p class="item-desc">Coconut Milk blended w/ Coconut Chunks, Bananas, Honey. Layered w/ Granola</p></div><span class="tag">$14.00</span></div>
    <div class="item"><div><p class="item-name">Coney Island</p><p class="item-desc">Apple Juice blended w/ Jackfruit, Mango and Pineapple.</p></div><span class="tag">$14.00</span></div>
    <div class="item"><div><p class="item-name">Coney Island</p><p class="item-desc">Apple Juice blended w/ Jackfruit, Mango and Pineapple.</p></div><span class="tag">$14.00</span></div>
    <div class="item"><div><p class="item-name">Main Street</p><p class="item-desc">Grade A Açaí, Choice of 1 of the following: Peanut, Almond, Cashew Butter and/or Hazelnut Spread, Granola, Bananas</p></div><span class="tag">$14.00</span></div>
  </div>

  <div class="hot-panel">
    <h2 class="section-title">Hot Food</h2>
    <div class="hot-cols">
      <div>
        <p class="hot-row"><span>Honey</span><span>$1.25</span></p>
        <p class="hot-row"><span>Extra Granola</span><span>$2.00</span></p>
        <p class="hot-row"><span>Gluten Free Granola</span><span>$2.25</span></p>
        <p class="hot-row"><span>Coconut Flakes</span><span>$2.00</span></p>
        <p class="hot-row"><span>Coconut Oil</span><span>$1.25</span></p>
        <p class="hot-row"><span>Bee Pollen</span><span>$2.00</span></p>
        <p class="hot-row"><span>Peanut Butter</span><span>$2.25</span></p>
      </div>
      <div>
        <p class="hot-row"><span>Honey</span><span>$1.25</span></p>
        <p class="hot-row"><span>Extra Granola</span><span>$2.00</span></p>
        <p class="hot-row"><span>Gluten Free Granola</span><span>$2.25</span></p>
        <p class="hot-row"><span>Coconut Flakes</span><span>$2.00</span></p>
        <p class="hot-row"><span>Coconut Oil</span><span>$1.25</span></p>
        <p class="hot-row"><span>Bee Pollen</span><span>$2.00</span></p>
        <p class="hot-row"><span>Peanut Butter</span><span>$2.25</span></p>
      </div>
    </div>
  </div>

  <div class="service-strip food-strip">
    <p><span><b>12 Oz Juices</b> and <b>2 Oz Shots</b></span><span>served in glass bottles.</span></p>
    <p class="strip-alt"><span><b>Gallon</b> and <b>1/2 Gallon</b> of our signature juices</span><span>available upon request.</span></p>
  </div>
  <p class="social"><span class="social-dot"></span>ThePulpCorner561</p>
</section>

</body>
</html>
```